Meadow Paw Web Site

We have basically a start up business that I need help with. This project is just for the web site.

Our product is a frozen raw pet food that promotes weight control, less shedding, smaller stools and an overall better health. The product is in nugget form similar to what you would see in a steak shish kabob. I only share that with you in case you want to incorporate that in the design.

We have been in business for 17 years but all of our sales have been word of mouth. We are going to be launching an infomercial this summer and I need everything stated previously to be completed before we can launch the infomercial.

We need the following (6) pages:

Home:
This is where we need to have the ability to purchase our products. Our main goal is to get the consumer to purchase our product. We have our own shopping cart so we just need to allow for the insertion of that shopping cart.

Why Raw:
This will just be a page with 4-5 paragraphs and an embedded YouTube video.

How to Use:
We will need a page with a chart (4 Columns wide with 6 rows) as well as an embedded YouTube video.

Customer Success Stories:
Allow us to add these as we move forward. I need a placeholder for an image of the customers pet and a paragraph or two explaining the situation

Where to Buy:
- Online - Find a Retailer - Find a Local Distributor - Call to Order

Contact Us:
Lantern Creek Companies, Inc.
2740 Lantern Cr
Eagan, MN 55122
(800) xxx-xxxx

We need to provide links to our to be created... Facebook page, Twitter Account, Youtube Channel, Google circle, Blog
Updates

All, I have received many front page designs that look good.  Please notice in the brief that I need multiple pages built not just the home page.  

Thanks,

Dale

Reason: I need to see the rest of the pages. Thanks, Dale

Target Market(s)

Women between the ages of 30 & 60.

Industry/Entity Type

Shopping

```html
<!DOCTYPE html>
<html lang="en">
<head>
<meta charset="utf-8">
<title>Meadow Paw – Home</title>
<link href="https://fonts.googleapis.com/css2?family=Open+Sans:wght@400;600;700&display=swap" rel="stylesheet">
<style>
:root{
  --ink:#1a1a1a;
  --muted:#7a7a7a;
  --body-text:#555;
  --accent:#c4470c;
  --accent-dark:#a83a08;
  --wood-light:#d07c45;
  --wood-dark:#b9622f;
  --rule:#d9d9d9;
  --black:#000;
  --white:#fff;
  --slide-band:#c9774b;
  --panel:#f7f2ee;
}
*{margin:0;padding:0;box-sizing:border-box}
html,body{width:670px;height:1200px;overflow:hidden;background:var(--white)}
body{font-family:"Open Sans",Arial,sans-serif;color:var(--ink)}
h1,h2,h3{font-weight:400}
.page{position:relative;width:670px;height:1200px;overflow:hidden}
.abs{position:absolute}

/* top bar */
.topbar{left:0;top:0;width:670px;height:24px;background:var(--black)}
.account-links{left:73px;top:7px;font-size:6.5px;font-weight:600;color:var(--white);white-space:nowrap}
.account-links span{margin:0 3px}
.social{display:flex;gap:3px}
.social i{display:block;width:15px;height:15px;border:1.2px solid var(--white);border-radius:50%;position:relative}
.social i::after{content:"";position:absolute;left:4.3px;top:4.3px;width:4px;height:4px;border-radius:50%;background:var(--white)}
.social-top{left:509px;top:4px}

/* header */
.header{left:0;top:24px;width:670px;height:385px;background:linear-gradient(90deg,var(--wood-dark),var(--wood-light) 50%,var(--wood-dark))}
.brand{left:72px;top:46px;display:flex;align-items:center;gap:6px;white-space:nowrap}
.brand-mark{width:14px;height:14px;background:var(--black)}
.brand-name{font-size:15px;font-weight:700;color:var(--black)}
.search{left:306px;top:49px;width:172px;height:18px;border:1px solid #e7b38f;background:#c9763f;display:flex}
.search-field{flex:1;font-size:6px;color:#f4dcc9;padding:4px 0 0 14px;position:relative;white-space:nowrap}
.search-field svg{position:absolute;left:4px;top:5px}
.search-btn{width:34px;background:#333;color:var(--white);font-size:7px;text-align:center;line-height:16px}
.cart-btn{left:490px;top:45px;width:107px;height:27px;background:var(--accent);color:var(--white);font-size:7px;font-weight:600;display:flex;align-items:center;padding-left:8px;gap:6px;white-space:nowrap}
.nav{left:284px;top:94px;display:flex;gap:16px;font-size:7.5px;color:var(--ink);white-space:nowrap}

/* slider */
.slider{left:73px;top:121px;width:525px;height:263px;border:1.5px solid #e6a77c}
.slide-panel{left:86px;top:134px;width:168px;height:236px;background:var(--panel)}
.slide-band{left:86px;top:338px;width:168px;height:32px;background:var(--slide-band)}
.slide-photo{left:254px;top:134px;width:332px;height:236px;background:linear-gradient(160deg,#ece8e3 0%,#d9c2a5 22%,#c4925f 45%,#b98654 70%,#d8cfc6 100%)}
.slide-title{left:96px;top:165px;font-size:12.5px;font-weight:600;line-height:16px;color:var(--accent);white-space:nowrap}
.slide-text{left:98px;top:210px;width:150px;font-size:7px;line-height:13.5px;color:#666}
.slide-btn{left:103px;top:291px;width:67px;height:22px;background:var(--black);color:var(--white);font-size:8px;text-align:center;line-height:22px}
.dots{left:146px;top:350px;display:flex;gap:2px}
.dots i{width:7px;height:7px;border-radius:50%;background:var(--white);border:1px solid #333}
.dots i:first-child{background:var(--black)}

/* products */
.product{top:428px;width:119px}
.product-photo{width:119px;height:83px;border:1px solid var(--rule)}
.photo-a{background:radial-gradient(ellipse at 55% 60%,#c99a5e,#e7d3b8 45%,#f6f4f1 75%)}
.photo-b{background:radial-gradient(ellipse at 50% 45%,#d7b58c,#f5f1ec 55%),linear-gradient(90deg,#6fbf4a,#fff 30%,#fff 70%,#6fbf4a)}
.photo-c{background:radial-gradient(ellipse at 50% 75%,#9a5a2c,#e39a35 35%,#f6f4f1 65%)}
.photo-d{background:radial-gradient(ellipse at 40% 60%,#d9b894,#f6f2ee 55%),radial-gradient(circle at 90% 15%,#e9a0a0,transparent 30%)}
.product-name{margin-top:7px;font-size:7.5px;font-weight:600;white-space:nowrap}
.product-desc{margin-top:9px;font-size:5.8px;line-height:12px;color:var(--muted)}
.product-rule{margin-top:6px;height:3px;border-top:1px solid var(--rule);border-bottom:1px solid var(--rule)}
.product-actions{margin-top:8px;display:flex;justify-content:space-between;font-size:6px;white-space:nowrap}
.add{color:var(--accent);display:flex;align-items:center;gap:3px}
.view{display:flex;align-items:center;gap:3px}
.view b{display:inline-block;width:6px;height:6px;background:var(--accent);color:var(--white);font-size:6px;line-height:6px;text-align:center}

.divider{left:73px;width:525px;height:1px;background:var(--rule)}

/* welcome */
.section-title{font-size:14px;color:var(--accent);white-space:nowrap}
.welcome-title{left:73px;top:626px}
.welcome-photo{left:73px;top:660px;width:148px;height:82px;border:1px solid var(--rule);background:radial-gradient(ellipse at 45% 25%,#b8643a,#f4f1ee 45%),linear-gradient(180deg,#f4f1ee 60%,#c98a55 85%,#a24636)}
.welcome-sub{left:227px;top:668px;font-size:7px;font-weight:600;white-space:nowrap}
.welcome-text{left:231px;top:685px;width:246px;font-size:6.2px;line-height:12.8px;color:var(--body-text)}
.mini-cart{left:490px;top:630px;width:106px;height:112px;border:1px solid var(--rule)}
.mini-cart-head{height:20px;background:#f2f2f2;border-bottom:1px solid var(--rule);font-size:7px;color:var(--accent);display:flex;justify-content:space-between;align-items:center;padding:0 8px 0 4px;white-space:nowrap}
.mini-cart-row{margin:0 7px;height:24px;border-bottom:1px dotted #bbb;font-size:5.8px;color:#666;display:flex;justify-content:space-between;align-items:center;white-space:nowrap}
.mini-cart-row.total{color:var(--ink);font-weight:600}
.checkout{margin:7px 0 0 7px;font-size:6px;color:var(--accent)}

/* stories */
.stories-title{left:0;top:778px;width:670px;text-align:center}
.stories-quote{left:0;top:802px;width:670px;text-align:center;font-size:6.2px;line-height:12px;color:#777}
.story-photo{left:74px;top:841px;width:199px;height:137px;border-radius:2px;background:linear-gradient(180deg,#8d5a2b 0%,#c9954e 18%,#efe8dd 40%,#d8cbb9 68%,#b23a2a 86%,#6e2a1d 100%)}
.story-title{left:291px;top:846px;font-size:9.5px;line-height:14px;color:var(--accent);white-space:nowrap}
.story-text{left:291px;top:884px;width:310px;font-size:6.2px;line-height:12.8px;color:var(--body-text)}
.story-btn{left:292px;top:950px;width:82px;height:21px;background:var(--accent-dark);color:var(--white);font-size:7px;font-weight:600;text-align:center;line-height:21px;white-space:nowrap}

/* footer */
.footer{left:0;top:1016px;width:670px;height:184px;background:var(--black)}
.footer svg.edge{position:absolute;left:0;top:-3px}
.foot-col{top:1042px;color:var(--white)}
.foot-col h3{font-size:10px;margin-bottom:8px;white-space:nowrap}
.foot-col li{list-style:none;font-size:6.3px;line-height:12.6px;white-space:nowrap}
.addr li{display:flex;gap:6px;align-items:center}
.addr li.plain{padding-left:12px}
.pay{display:flex;gap:3px}
.pay i{width:22px;height:12px;background:#ddd;border-radius:1px}
.pay i:nth-child(2){background:#f4f4f4}
.pay i:nth-child(4){background:#2b7fc1}
.follow{margin-top:16px}
.footer-rule{left:73px;top:1156px;width:525px;height:1px;background:#222}
.copyright{left:0;top:1174px;width:670px;text-align:center;font-size:6.3px;color:var(--white)}
</style>
</head>
<body>
<div class="page">

  <div class="abs topbar"></div>
  <div class="abs account-links">Login<span>|</span>Register<span>|</span>Account</div>
  <div class="abs social social-top" aria-label="Social links"><i></i><i></i><i></i><i></i><i></i></div>

  <header class="abs header"></header>
  <div class="abs brand"><span class="brand-mark"></span><span class="brand-name">Meadow Paw</span></div>
  <div class="abs search">
    <div class="search-field"><svg width="7" height="7" viewBox="0 0 7 7"><circle cx="3" cy="3" r="2" fill="none" stroke="#fff" stroke-width="1"/><line x1="4.5" y1="4.5" x2="6.5" y2="6.5" stroke="#fff"/></svg>Enter any keyword</div>
    <div class="search-btn">Search</div>
  </div>
  <div class="abs cart-btn">
    <svg width="13" height="11" viewBox="0 0 13 11"><path d="M0 1h2.5l2 6h6l2-4.5H4" fill="none" stroke="#fff" stroke-width="1.4"/><circle cx="5.5" cy="9.5" r="1.2" fill="#fff"/><circle cx="9.5" cy="9.5" r="1.2" fill="#fff"/></svg>
    <span>Shopping Cart (0)</span>
    <svg width="6" height="4" viewBox="0 0 6 4" style="margin-left:4px"><path d="M0 0l3 3 3-3" fill="none" stroke="#fff" stroke-width="1.2"/></svg>
  </div>
  <nav class="abs nav"><span>Home</span><span>Why RAW</span><span>How to Use</span><span>Success Stories</span><span>Where to Buy</span><span>Contact us</span></nav>

  <div class="abs slider"></div>
  <div class="abs slide-photo" role="img" aria-label="Homemade raw dog treat dough with bone-shaped cutter and rolling pin"></div>
  <div class="abs slide-panel"></div>
  <div class="abs slide-band"></div>
  <h1 class="abs slide-title">Neque porro quisquam<br>Est qui dolorem ipsum</h1>
  <p class="abs slide-text">At vero eos et accusamus et iusto klodi dignissimos ducimus qui blanditiis praes ntium voluptatum deleniti atque corrupti quos dolores et quas molestias excepturi s int occaecati cupiditate non provident,</p>
  <div class="abs slide-btn">View More</div>
  <div class="abs dots"><i></i><i></i><i></i><i></i><i></i></div>

  <div class="abs product" style="left:73px">
    <div class="product-photo photo-a" role="img" aria-label="Puppy chewing a raw bone"></div>
    <div class="product-name">Neque porro quisquav bmui do</div>
    <div class="product-desc">Diets come and diets cgo. We have all he ard about fad diets for humans</div>
    <div class="product-rule"></div>
    <div class="product-actions"><span class="add"><svg width="9" height="8" viewBox="0 0 13 11"><path d="M0 1h2.5l2 6h6l2-4.5H4" fill="none" stroke="#c4470c" stroke-width="1.6"/><circle cx="5.5" cy="9.5" r="1.3" fill="#c4470c"/><circle cx="9.5" cy="9.5" r="1.3" fill="#c4470c"/></svg>Add To cart</span><span class="view"><b>+</b>View Here</span></div>
  </div>
  <div class="abs product" style="left:206px">
    <div class="product-photo photo-b" role="img" aria-label="Bulldog seated between two food bowls"></div>
    <div class="product-name">Neque porro quisquav bmui do</div>
    <div class="product-desc">Diets come and diets cgo. We have all he ard about fad diets for humans</div>
    <div class="product-rule"></div>
    <div class="product-actions"><span class="add"><svg width="9" height="8" viewBox="0 0 13 11"><path d="M0 1h2.5l2 6h6l2-4.5H4" fill="none" stroke="#c4470c" stroke-width="1.6"/><circle cx="5.5" cy="9.5" r="1.3" fill="#c4470c"/><circle cx="9.5" cy="9.5" r="1.3" fill="#c4470c"/></svg>Add To cart</span><span class="view"><b>+</b>View Here</span></div>
  </div>
  <div class="abs product" style="left:341px">
    <div class="product-photo photo-c" role="img" aria-label="Puppy behind a bowl of raw food nuggets"></div>
    <div class="product-name">Neque porro quisquav bmui do</div>
    <div class="product-desc">Diets come and diets cgo. We have all he ard about fad diets for humans</div>
    <div class="product-rule"></div>
    <div class="product-actions"><span class="add"><svg width="9" height="8" viewBox="0 0 13 11"><path d="M0 1h2.5l2 6h6l2-4.5H4" fill="none" stroke="#c4470c" stroke-width="1.6"/><circle cx="5.5" cy="9.5" r="1.3" fill="#c4470c"/><circle cx="9.5" cy="9.5" r="1.3" fill="#c4470c"/></svg>Add To cart</span><span class="view"><b>+</b>View Here</span></div>
  </div>
  <div class="abs product" style="left:478px">
    <div class="product-photo photo-d" role="img" aria-label="Bulldog looking at a piece of raw meat"></div>
    <div class="product-name">Neque porro quisquav bmui do</div>
    <div class="product-desc">Diets come and diets cgo. We have all he ard about fad diets for humans</div>
    <div class="product-rule"></div>
    <div class="product-actions"><span class="add"><svg width="9" height="8" viewBox="0 0 13 11"><path d="M0 1h2.5l2 6h6l2-4.5H4" fill="none" stroke="#c4470c" stroke-width="1.6"/><circle cx="5.5" cy="9.5" r="1.3" fill="#c4470c"/><circle cx="9.5" cy="9.5" r="1.3" fill="#c4470c"/></svg>Add To cart</span><span class="view"><b>+</b>View Here</span></div>
  </div>

  <div class="abs divider" style="top:607px"></div>

  <h2 class="abs section-title welcome-title">Welcome To&nbsp; Meadow Paw</h2>
  <div class="abs welcome-photo" role="img" aria-label="Dog behind a board with kibble and raw meat"></div>
  <h3 class="abs welcome-sub">Neque porro quisquam est qui dolorem ipsum quia dolor sit amet</h3>
  <p class="abs welcome-text">Lorem ipsum dolor sit amet, consectetur adipisicing elit, sed do eiusmod tempor in cididunt ut labore et dolore magna aliqua. Ut enim ad minim veniam, quis nostru d exercitation ullamco laboris nisi ut aliquip ex ea commodo consequat. Duis aute ir ure dolor in reprehenderit in voluptate velit esse cillum</p>

  <aside class="abs mini-cart">
    <div class="mini-cart-head">Our Shopping Cart<svg width="9" height="8" viewBox="0 0 13 11"><path d="M0 1h2.5l2 6h6l2-4.5H4" fill="none" stroke="#c4470c" stroke-width="1.6"/><circle cx="5.5" cy="9.5" r="1.3" fill="#c4470c"/><circle cx="9.5" cy="9.5" r="1.3" fill="#c4470c"/></svg></div>
    <div class="mini-cart-row"><span>Number Of Products</span><span>( 0.00 )</span></div>
    <div class="mini-cart-row"><span>Shopping Cart</span><span>( 0.00 )</span></div>
    <div class="mini-cart-row total"><span>Total</span><span>( 0.00 )</span></div>
    <div class="checkout">Check Out</div>
  </aside>

  <div class="abs divider" style="top:767px"></div>

  <h2 class="abs section-title stories-title">Our Success Stories</h2>
  <p class="abs stories-quote">Neque porro quisquam est qui dolorem ipsum quia dolor sit amet, consectetur, adipisci velit..."<br>"There is no one who loves pain itself, who seeks after it and wants to have it, simply because it is pain.</p>
  <div class="abs story-photo" role="img" aria-label="Small white terrier resting on a rug"></div>
  <h3 class="abs story-title">Neque porro quisquam est qui dolorem ipsum<br>quia dolor sit amet, consectetur</h3>
  <p class="abs story-text">Lorem ipsum dolor sit amet, consectetur adipisicing elit, sed do eiusmod tUt enim ad mUt enim ad mem cididunt ut labore et dolore magna aliqua. Ut enim ad minim veniam, quis nUt Ut enim ad menim ad mos d exercitation ullamco laboris nisi ut aliquip ex ea commodo consequat. DuisUt enim ad m auteUt enimh ure dolor in reprehenderit in voluptate velit esse cillum.</p>
  <div class="abs story-btn">View More Stories</div>

  <footer class="abs footer">
    <svg class="edge" width="670" height="4" viewBox="0 0 670 4" preserveAspectRatio="none"><pattern id="zig" width="4" height="4" patternUnits="userSpaceOnUse"><path d="M0 4L2 0 4 4z" fill="#000"/></pattern><rect width="670" height="4" fill="url(#zig)"/></svg>
  </footer>
  <div class="abs foot-col" style="left:73px">
    <h3>Information</h3>
    <ul><li>Home</li><li>Why RAW</li><li>How to Use</li><li>Success Stories</li><li>Where to Buy</li><li>Contact us</li></ul>
  </div>
  <div class="abs foot-col" style="left:209px">
    <h3>My Account</h3>
    <ul><li>My Account</li><li>Order History</li><li>&nbsp;Wish List</li><li>Newsletter</li><li>Shopping Cart</li></ul>
  </div>
  <div class="abs foot-col addr" style="left:350px">
    <h3 style="padding-left:1px">Address</h3>
    <ul>
      <li><svg width="8" height="7" viewBox="0 0 8 7"><path d="M4 0L0 3.5h1V7h2.2V5h1.6v2H7V3.5h1z" fill="#fff"/></svg>Meadow Paw, LLC</li>
      <li class="plain">418 Willow Bend Rd., #12</li>
      <li class="plain">Fernhill, CA 95500</li>
      <li><svg width="7" height="7" viewBox="0 0 7 7"><path d="M1.5 0l1.3 1.8-.8 1a4 4 0 002 2l1-.8L7 5.5 6 7C3 7 0 4 0 1z" fill="#fff"/></svg>Call us: 555-014-2290</li>
      <li><svg width="7" height="5" viewBox="0 0 7 5"><rect width="7" height="5" fill="#fff"/><path d="M0 0l3.5 2.8L7 0" fill="none" stroke="#000" stroke-width=".7"/></svg>Email us: info@meadowpawfoods.com</li>
    </ul>
  </div>
  <div class="abs foot-col" style="left:496px">
    <h3>Payment Block</h3>
    <div class="pay" aria-label="Accepted payment cards"><i></i><i></i><i></i><i></i></div>
    <h3 class="follow">Follow Us</h3>
    <div class="social" aria-label="Social links"><i></i><i></i><i></i><i></i><i></i></div>
  </div>
  <div class="abs footer-rule"></div>
  <div class="abs copyright">Copyright © 2014 all rights are reserved</div>

</div>
</body>
</html>
```